Stationery Design For Specialist London law firm

We have merged two firms of London lawyers to create a new firm with a new name.

The new firms name is RT Hollby. We would like to include the description Solicitors and Advocates in the design.

We need a new design for our headed paper, business cards compliment slips etc.

The image we wish to project is fresh but not gimmicky - reliable and strong but not stuffy.

We have no strong views on font or colour this really is pretty much a blank page.

Our preference is for the name to be at the top of the page

Target Market(s)

Our clients who are individuals rather than corporate and other lawyers

Industry/Entity Type

Law Firm

Requirements
Should not have
• Legal images eg scales of justice etc

Obviously nothing childish or gimmicky

```html
<!DOCTYPE html>
<html lang="en">
<head>
<meta charset="utf-8">
<title>RT Hollby – Business Cards</title>
<link rel="stylesheet" href="https://fonts.googleapis.com/css2?family=Gelasio:wght@400;700&family=Arimo:wght@400&display=swap">
<style>
  :root {
    --backdrop: #4b4b4b;
    --card: #000000;
    --brand-blue: #1f6fb8;
    --rule-blue: #3f6a93;
    --text-light: #f2f2f2;
    --mark-light: #f2f2f2;
  }
  html, body {
    margin: 0;
    width: 1200px;
    height: 900px;
    overflow: hidden;
    background: var(--backdrop);
  }
  .stage { position: relative; width: 1200px; height: 900px; }
  .card {
    position: absolute;
    top: 300px;
    width: 525px;
    height: 300px;
    background: var(--card);
    border-radius: 22px;
    overflow: hidden;
    font-family: "Arimo", Arial, sans-serif;
    color: var(--text-light);
  }
  .card--front { left: 58px; }
  .card--back { left: 617px; }

  .brand { position: absolute; display: flex; align-items: center; }
  .brand__square { background: var(--brand-blue); flex: none; }
  .brand__divider { background: #8a8a8a; width: 1px; flex: none; }
  .brand__name {
    font-family: "Gelasio", Georgia, serif;
    font-weight: 700;
    color: var(--brand-blue);
    line-height: 1;
    white-space: nowrap;
  }
  .brand__tagline {
    font-family: "Gelasio", Georgia, serif;
    color: var(--text-light);
    line-height: 1;
    white-space: nowrap;
  }

  .card--front .brand { left: 79px; top: 104px; }
  .card--front .brand__square { width: 82px; height: 90px; }
  .card--front .brand__divider { height: 73px; margin: 0 15px 0 16px; }
  .card--front .brand__name { font-size: 48px; }
  .card--front .brand__tagline { font-size: 22px; margin-top: 2px; }

  .card--back .brand { left: 52px; top: 58px; }
  .card--back .brand__square { width: 51px; height: 56px; }
  .card--back .brand__divider { height: 44px; margin: 0 8px 0 9px; }
  .card--back .brand__name { font-size: 29px; }
  .card--back .brand__tagline { font-size: 13.5px; margin-top: 1px; }

  .footer-rule {
    position: absolute;
    left: 0;
    top: 266px;
    height: 2px;
    background: var(--rule-blue);
  }
  .card--front .footer-rule { width: 324px; }
  .card--back .footer-rule { width: 323px; }
  .website {
    position: absolute;
    top: 258px;
    font-size: 14px;
    letter-spacing: 1.3px;
    color: var(--text-light);
  }
  .card--front .website { left: 332px; }
  .card--back .website { left: 331px; }

  .contact {
    position: absolute;
    left: 52px;
    top: 166px;
    font-size: 13px;
    line-height: 17px;
  }
  .contact__address { font-size: 13.5px; margin-bottom: 3px; }
  .contact__label { color: var(--brand-blue); }
  .contact__gap { display: inline-block; width: 8px; }

  .person {
    position: absolute;
    right: 27px;
    top: 166px;
    text-align: right;
  }
  .person__name { font-size: 18px; color: var(--brand-blue); line-height: 20px; }
  .person__role { font-size: 11px; line-height: 14px; }
  .person-tab {
    position: absolute;
    right: 0;
    top: 165px;
    width: 13px;
    height: 33px;
    background: var(--brand-blue);
    border-radius: 4px 0 0 4px;
  }
</style>
</head>
<body>
<main class="stage">
  <section class="card card--front" aria-label="Business card front">
    <div class="brand">
      <div class="brand__square"></div>
      <div class="brand__divider"></div>
      <div class="brand__text">
        <div class="brand__name">RT Hollby</div>
        <div class="brand__tagline">Solicitors and Advocates</div>
      </div>
    </div>
    <div class="footer-rule"></div>
    <div class="website">www.rthollby.com</div>
  </section>

  <section class="card card--back" aria-label="Business card back">
    <div class="brand">
      <div class="brand__square"></div>
      <div class="brand__divider"></div>
      <div class="brand__text">
        <div class="brand__name">RT Hollby</div>
        <div class="brand__tagline">Solicitors and Advocates</div>
      </div>
    </div>
    <div class="contact">
      <div class="contact__address">00000 RT Hollby, Your Address 00000</div>
      <div><span class="contact__label">p:</span> 555-310-4821<span class="contact__gap"></span><span class="contact__label">m:</span> 555-310-4822</div>
      <div><span class="contact__label">f:</span> 555-310-4823<span class="contact__gap"></span><span class="contact__label">e:</span> mail@rthollby.com</div>
    </div>
    <div class="person">
      <div class="person__name">Marian Callow</div>
      <div class="person__role">Owner</div>
    </div>
    <div class="person-tab"></div>
    <div class="footer-rule"></div>
    <div class="website">www.rthollby.com</div>
  </section>
</main>
</body>
</html>
```